TALRENO Business Cards

We require a business card for our company that provides IT consulting services. We already have a logo that needs to be used on the card. We want a clean professional looking design that incorporates our colours. Our main focus is providing managed services to business, which involves us looking after all of their IT requirements including managing servers/networks, projects, and procurement.

Industry/Entity Type

Information Technology

Requirements
Must have
• our logo, contact information, name, title, phone numbers

```html
<!DOCTYPE html>
<html lang="en">
<head>
<meta charset="utf-8">
<title>TALRENO Business Cards</title>
<link href="https://fonts.googleapis.com/css2?family=Open+Sans:wght@400;600;700&display=swap" rel="stylesheet">
<style>
  :root {
    --brand-blue: #1592d0;
    --ink: #3a3a3a;
    --card-white: #ffffff;
    --backdrop: #e9e6e3;
  }
  * { box-sizing: border-box; margin: 0; padding: 0; }
  html, body { width: 1200px; height: 997px; overflow: hidden; }
  body {
    background: var(--backdrop);
    font-family: "Open Sans", Arial, sans-serif;
    display: flex;
    align-items: center;
    justify-content: center;
    gap: 48px;
  }
  .card {
    position: relative;
    width: 540px;
    height: 309px;
    background: var(--card-white);
    box-shadow: 0 2px 10px rgba(0,0,0,0.12);
    overflow: hidden;
  }
  /* Front card */
  .top-stripe {
    position: absolute;
    top: 30px; left: 300px; right: 0;
    height: 16px;
    background: var(--brand-blue);
  }
  .name-tab {
    position: absolute;
    top: 30px; left: 278px;
    width: 196px; height: 52px;
    background: var(--brand-blue);
    border-radius: 0 0 0 14px;
    color: var(--card-white);
    padding: 5px 0 0 16px;
  }
  .name-tab .person-name {
    font-size: 17px;
    font-weight: 400;
    letter-spacing: 0.3px;
    line-height: 1.3;
  }
  .name-tab .person-title {
    font-size: 11px;
    line-height: 1.2;
  }
  .bottom-stripe {
    position: absolute;
    left: 0; right: 0; bottom: 16px;
    height: 9px;
    background: var(--brand-blue);
  }
  .front-brand {
    position: absolute;
    left: 70px; top: 132px;
    display: flex; align-items: center; gap: 10px;
  }
  .brand-dot {
    width: 22px; height: 22px;
    border-radius: 50%;
    background: var(--brand-blue);
    flex: none;
  }
  .brand-name {
    color: var(--brand-blue);
    font-weight: 700;
    font-size: 30px;
    letter-spacing: 2px;
    line-height: 1;
  }
  .contact {
    position: absolute;
    left: 300px; top: 102px;
    color: var(--ink);
    font-size: 12px;
    line-height: 1.45;
  }
  .contact .address { margin-bottom: 12px; }
  .contact-line { display: flex; align-items: center; gap: 7px; }
  .contact-line svg { width: 10px; height: 10px; fill: var(--brand-blue); flex: none; }
  /* Back card */
  .card-back {
    display: flex; align-items: center; justify-content: center;
  }
  .back-brand { display: flex; align-items: center; gap: 14px; }
  .back-brand .brand-dot { width: 34px; height: 34px; }
  .back-brand .brand-name { font-size: 46px; letter-spacing: 4px; }
</style>
</head>
<body>
  <section class="card card-front">
    <div class="top-stripe"></div>
    <div class="name-tab">
      <p class="person-name">MARCUS HALE</p>
      <p class="person-title">Founder &amp; CEO</p>
    </div>
    <div class="front-brand">
      <span class="brand-dot"></span>
      <span class="brand-name">TALRENO</span>
    </div>
    <div class="contact">
      <p class="address">Po Box-123, Street Name,<br>City Name, Zip Code - 00000</p>
      <p class="contact-line">
        <svg viewBox="0 0 10 10"><path d="M2 0.5 L3.8 2.6 L2.9 3.7 Q4 5.9 6.3 7.1 L7.4 6.2 L9.5 8 L8.4 9.5 Q2.8 8.8 0.5 1.6 Z"/></svg>
        +44 7700 900123
      </p>
      <p class="contact-line">
        <svg viewBox="0 0 10 10"><path d="M0 2 H10 V8.5 H0 Z M0.6 2.4 L5 5.6 L9.4 2.4 V3.3 L5 6.5 L0.6 3.3 Z" fill-rule="evenodd"/></svg>
        marcus@talreno-it.com
      </p>
      <p class="contact-line">
        <svg viewBox="0 0 10 10"><circle cx="5" cy="5" r="4.6"/><path d="M0.6 5 H9.4 M5 0.4 V9.6 M5 0.4 Q2.2 5 5 9.6 M5 0.4 Q7.8 5 5 9.6" stroke="#fff" stroke-width="0.7" fill="none"/></svg>
        www.talreno-it.com
      </p>
    </div>
    <div class="bottom-stripe"></div>
  </section>

  <section class="card card-back">
    <div class="back-brand">
      <span class="brand-dot"></span>
      <span class="brand-name">TALRENO</span>
    </div>
  </section>
</body>
</html>
```